New Business Card for Auto Repair and Performance Shop!

Need a redesign on a card that we have used for a while now. Something more update and modern, Serious but not too serious. Something confident, that shows the client that we are bespoke. Adding value.

Target Market(s)

Foreign Auto Repair and Performance

Industry/Entity Type

Automotive

Contact Information for Business Card

Utilize Logo, would like to change car silhouette to something Verso,

Font styles to use
Sans Serif

Requirements
Must have
• business name, address, website, phone number.
MotoRadiance
5182 W. Birchfold Rd
Corvane, T.X. 70418
1-555-468-3172
www.moto-radence.example

Focused on Asian, European, and Domestic Car Service, Performance Tuning and Custom Builds.

Clear space on back to for space to write appointment time and which client advisor helped the client.
Nice to have
• Up to the designers,

```html
<!DOCTYPE html>
<html lang="en">
<head>
<meta charset="utf-8">
<title>MotoRadiance – Business Card</title>
<link rel="stylesheet" href="https://fonts.googleapis.com/css2?family=Roboto+Condensed:wght@400;700&display=swap">
<style>
  :root {
    --page: #d9d9db;
    --card-base: #1b1b1d;
    --card-shade: #141415;
    --card-facet: #232326;
    --card-facet-light: #2b2b2f;
    --brand-red: #c8202a;
    --text-light: #d4d4d6;
    --text-white: #ffffff;
  }
  * { box-sizing: border-box; margin: 0; padding: 0; }
  html, body { width: 1200px; height: 900px; overflow: hidden; }
  body {
    background: var(--page);
    font-family: "Roboto Condensed", Arial, sans-serif;
    position: relative;
  }
  .card {
    position: absolute;
    left: 250px;
    width: 700px;
    height: 400px;
    background: var(--card-base);
    overflow: hidden;
    box-shadow: 0 10px 30px rgba(0,0,0,.25);
  }
  .card--front { top: 40px; }
  .card--back { top: 460px; }
  .card__facets { position: absolute; inset: 0; width: 100%; height: 100%; }

  .brand-name {
    position: absolute;
    font-family: "Roboto Condensed", Arial, sans-serif;
    font-weight: 700;
    font-size: 36px;
    color: var(--text-white);
    letter-spacing: .5px;
    line-height: 1;
  }
  .card--front .brand-name { left: 220px; top: 122px; }
  .card--back .brand-name { left: 240px; top: 188px; }

  .contact {
    position: absolute;
    left: 150px;
    top: 205px;
    display: flex;
    align-items: center;
    color: var(--text-light);
    font-size: 17px;
    line-height: 1.35;
  }
  .contact__address { display: flex; align-items: center; gap: 10px; margin-top: 40px; font-style: normal; }
  .contact__divider {
    width: 3px;
    height: 82px;
    background: var(--brand-red);
    margin: 0 22px 0 34px;
  }
  .contact__lines { display: flex; flex-direction: column; gap: 4px; margin-bottom: 30px; }
  .contact__item { display: flex; align-items: center; gap: 8px; }
  .icon { width: 16px; height: 16px; flex: none; }
  .icon--pin { width: 18px; height: 22px; }

  .tagline-band {
    position: absolute;
    left: 0;
    bottom: 0;
    width: 100%;
    height: 90px;
  }
  .tagline {
    position: absolute;
    left: 36px;
    bottom: 14px;
    font-weight: 700;
    font-size: 15.5px;
    color: var(--text-white);
    letter-spacing: .2px;
    white-space: nowrap;
  }
  .back-edge {
    position: absolute;
    left: 0; top: 0;
    width: 100%;
    height: 8px;
    background: var(--brand-red);
  }
</style>
</head>
<body>

<section class="card card--front" aria-label="Business card front">
  <svg class="card__facets" viewBox="0 0 700 400" aria-hidden="true">
    <polygon points="0,0 700,0 700,40 470,40 380,0" fill="var(--card-shade)"/>
    <polygon points="0,40 220,0 330,0 90,140 0,140" fill="var(--card-facet)"/>
    <polygon points="480,140 700,90 700,250 560,250" fill="var(--card-facet)"/>
    <polygon points="0,250 120,250 60,330 0,330" fill="var(--card-facet-light)"/>
    <polygon points="380,40 700,40 700,90 470,140" fill="var(--card-facet-light)" opacity=".5"/>
  </svg>

  <p class="brand-name">MotoRadiance</p>

  <div class="contact">
    <address class="contact__address">
      <svg class="icon icon--pin" viewBox="0 0 18 22" aria-hidden="true">
        <path d="M9 0C4 0 0 4 0 9c0 6 9 13 9 13s9-7 9-13c0-5-4-9-9-9zm0 12.5A3.5 3.5 0 1 1 9 5.5a3.5 3.5 0 0 1 0 7z" fill="var(--brand-red)"/>
      </svg>
      <span>5182 W. Birchfold Rd,<br>Corvane, T.X. 70418</span>
    </address>
    <span class="contact__divider"></span>
    <div class="contact__lines">
      <div class="contact__item">
        <svg class="icon" viewBox="0 0 16 16" aria-hidden="true">
          <path d="M3.5 1l2.5 3-1.6 1.8c.9 2 2.4 3.5 4.3 4.4L10.5 8.6l3 2.5-1.4 2.6C7 13.4 2.6 9 2.3 3.9z" fill="var(--brand-red)"/>
        </svg>
        <span>1-555-468-3172</span>
      </div>
      <div class="contact__item">
        <svg class="icon" viewBox="0 0 16 16" aria-hidden="true">
          <g fill="none" stroke="var(--brand-red)" stroke-width="1.5">
            <circle cx="8" cy="8" r="6.5"/>
            <ellipse cx="8" cy="8" rx="2.8" ry="6.5"/>
            <line x1="1.5" y1="8" x2="14.5" y2="8"/>
          </g>
        </svg>
        <span>www.moto-radence.example</span>
      </div>
    </div>
  </div>

  <svg class="tagline-band" viewBox="0 0 700 90" preserveAspectRatio="none" aria-hidden="true">
    <polygon points="0,48 280,48 290,40 700,40 700,90 0,90" fill="var(--brand-red)"/>
    <polygon points="470,40 480,22 700,0 700,40" fill="var(--brand-red)"/>
  </svg>
  <p class="tagline">Focused on Asian, European, and Domestic Car Service, Performance Tuning and Custom Builds.</p>
</section>

<section class="card card--back" aria-label="Business card back">
  <span class="back-edge"></span>
  <svg class="card__facets" viewBox="0 0 700 400" aria-hidden="true" style="top:8px">
    <polygon points="0,40 200,0 360,0 120,130 0,130" fill="var(--card-facet)"/>
    <polygon points="0,240 180,240 100,330 0,330" fill="var(--card-facet)"/>
    <polygon points="540,260 700,220 700,330 600,330" fill="var(--card-facet-light)"/>
    <polygon points="360,330 700,330 700,392 300,392" fill="var(--card-shade)"/>
  </svg>
  <p class="brand-name">MotoRadiance</p>
</section>

</body>
</html>
```